Build Website for Playful Brand that helps content creators build businesses

Please help me create a website for my company that helps content creators build businesses around their audience. I have attached a design and vibe that I am going for at quillmoth.io.

Open for changes, but I want to keep the colour I currently have (a light teal). Ultimately the brand is playful but should come off as a very modern elevated brand.

I am looking for a few pages including

1. Home (with clear CTA button)
A section where I can input what the company does, and some brands that we have launched

2. About Me
A simple page, that has preferably able to put a circular image of myself and then give a quick background about the company

3. Blog (can you include how blog posts will appear and it should sit nicely in the page)
This ideally is a section that will be able to link to another software so my blogs automatically flow into here or posts. But otherwise it should have sections of blocks where creators can see about topics that I post about

4. Contact (this should include a form that will allow users to contact me)
Finally a contact page where it links my socials, similar what is there, but ideally there is a form they can fill out which I can link to my inbox as well. This should be a simple page as well

Create a multi page website, including a page that will link or can link blog post

Similar to this vibe and logo - https://quillmoth.io/

Target Market(s)

Content Creators

Coding

Coded - Design and coding required

Number of Pages Required

4 page

Requirements
Must have
• Home, Contact Me (Including a place to submit an enquiry and form), Blog Post Page As well

```html
<!DOCTYPE html>
<html lang="en">
<head>
<meta charset="utf-8">
<title>Quill Moth — Building Businesses</title>
<link rel="stylesheet" href="https://fonts.googleapis.com/css2?family=Outfit:wght@300;400;500;600&display=swap">
<style>
:root{
  --ink:#2f5460;
  --ink-dark:#2b2b2b;
  --text:#3a3a3a;
  --muted:#8a9aa0;
  --hero-bg:#e8fcfc;
  --blob:#cbe8f0;
  --blob-soft:#e3f4f8;
  --teal:#3cc6d6;
  --footer-bg:#cdedf3;
  --bar:#2f4f5a;
  --white:#ffffff;
  --pill:#5a8592;
  --card-shadow:0 2px 10px rgba(0,0,0,.08);
}
*{box-sizing:border-box;margin:0;padding:0}
html,body{width:1200px;height:3256px;overflow:hidden}
body{position:relative;background:var(--white);font-family:"Outfit",sans-serif;color:var(--text)}
a{color:inherit;text-decoration:none}

/* header */
.site-header{position:absolute;left:0;top:0;width:1200px;height:125px;background:var(--white);z-index:2}
.logo-disc{position:absolute;left:32px;top:-80px;width:316px;height:308px;border-radius:50%;background:var(--white);z-index:1}
.logo-mark{position:absolute;left:158px;top:26px;width:64px;height:64px;border-radius:50%;background:var(--blob);z-index:3}
.logo-name{position:absolute;left:60px;top:132px;width:260px;text-align:center;font-size:27px;letter-spacing:3px;color:var(--ink);font-weight:400;line-height:34px;z-index:3}
.main-nav{position:absolute;top:56px;font-size:16px;color:var(--ink);font-weight:400}
.main-nav a{position:absolute;white-space:nowrap}
.main-nav .active{border-bottom:2px solid var(--ink);padding-bottom:10px}
.btn{position:absolute;display:flex;align-items:center;background:var(--ink);color:var(--white);border-radius:40px;font-weight:500;white-space:nowrap}
.btn .arrow{position:absolute;right:6px;top:50%;transform:translateY(-50%);border-radius:50%;background:var(--pill);display:flex;align-items:center;justify-content:center}
.nav-cta{left:976px;top:42px;width:149px;height:50px;justify-content:center;font-size:17px}

/* hero */
.hero{position:absolute;left:0;top:125px;width:1200px;height:626px;background:var(--hero-bg)}
.hero h1{position:absolute;left:110px;top:152px;font-weight:500;line-height:1;font-size:100px;color:var(--ink);letter-spacing:-1px}
.hero h1 span{display:block;color:var(--ink-dark);font-size:80px;margin-top:10px}
.hero .lede{position:absolute;left:117px;top:356px;font-size:20px;color:var(--ink-dark)}
.hero-cta{left:118px;top:415px;width:189px;height:56px;padding-left:34px;font-size:17px}
.hero-art{position:absolute;left:623px;top:41px;width:532px;height:532px;border-radius:50%;background:var(--white);overflow:hidden}
.hero-art .scene{position:absolute;left:56px;top:70px;width:430px;height:410px;border-radius:50%;
  background:
    radial-gradient(circle at 30% 28%,rgba(250,120,110,.55),rgba(250,120,110,0) 28%),
    radial-gradient(circle at 48% 62%,rgba(70,110,200,.45),rgba(70,110,200,0) 30%),
    radial-gradient(circle at 72% 58%,rgba(120,70,90,.40),rgba(120,70,90,0) 30%),
    radial-gradient(circle at 16% 72%,rgba(110,170,80,.45),rgba(110,170,80,0) 22%),
    radial-gradient(circle at 80% 32%,rgba(240,200,110,.40),rgba(240,200,110,0) 22%),
    linear-gradient(160deg,#f3f4f7,#e6e7ec)}

/* section titles */
.title{position:absolute;font-weight:500;font-size:60px;color:var(--ink);line-height:1}
.rule{position:absolute;height:3px;background:linear-gradient(90deg,var(--blob),rgba(203,232,240,0))}
.rule.rev{background:linear-gradient(270deg,var(--blob),rgba(203,232,240,0))}

/* about */
.about-blob{position:absolute;left:76px;top:835px;width:420px;height:436px;border-radius:48% 52% 40% 60%/55% 45% 55% 45%;background:linear-gradient(150deg,var(--blob),var(--blob-soft))}
.about-frame{position:absolute;left:186px;top:942px;width:306px;height:236px;border:3px dashed var(--teal);border-radius:8px;
  background:
    radial-gradient(circle at 30% 60%,rgba(240,80,150,.35),rgba(240,80,150,0) 30%),
    radial-gradient(circle at 62% 58%,rgba(60,190,200,.35),rgba(60,190,200,0) 30%),
    radial-gradient(circle at 72% 40%,rgba(230,160,80,.35),rgba(230,160,80,0) 22%),
    #f1f9fb}
.about-ground{position:absolute;left:180px;top:1270px;width:330px;height:2px;background:#5b2f3a}
.about-tag{position:absolute;left:597px;top:976px;width:530px;font-size:19px;line-height:29px;color:var(--ink-dark)}
.about-copy{position:absolute;left:597px;top:1054px;width:527px;font-size:16px;line-height:27px;text-align:justify;font-weight:300;color:var(--text)}
.about-cta{left:597px;top:1220px;width:163px;height:50px;padding-left:25px;font-size:16px}

/* blog */
.blog-intro{position:absolute;left:190px;top:1494px;width:820px;text-align:center;font-size:16px;line-height:27px;font-weight:300;color:var(--text)}
.post-card{position:absolute;top:1602px;width:314px;height:598px;background:var(--white);box-shadow:var(--card-shadow)}
.post-body{position:absolute;left:32px;width:270px}
.post-date{font-size:14px;color:var(--ink);display:flex;align-items:center;gap:6px}
.post-title{margin-top:14px;font-size:18.5px;line-height:28px;font-weight:500;color:var(--ink-dark)}
.post-excerpt{margin-top:12px;font-size:14px;line-height:24px;font-weight:300;color:var(--text)}
.post-btn{position:relative;margin-top:16px;width:115px;height:35px;padding-left:17px;font-size:11px}
.post-img{position:absolute;left:6px;width:302px;height:292px}
.img-search{background:
  radial-gradient(circle at 50% 50%,rgba(140,160,220,.55),rgba(140,160,220,0) 40%),
  radial-gradient(circle at 25% 75%,rgba(240,200,90,.5),rgba(240,200,90,0) 25%),
  radial-gradient(circle at 68% 52%,rgba(240,150,90,.45),rgba(240,150,90,0) 18%),
  linear-gradient(160deg,#f1ece2,#e7e2d6)}
.img-brand{background:
  radial-gradient(circle at 20% 10%,rgba(240,150,80,.55),rgba(240,150,80,0) 28%),
  radial-gradient(circle at 88% 72%,rgba(245,90,70,.55),rgba(245,90,70,0) 22%),
  radial-gradient(circle at 50% 40%,rgba(60,50,120,.45),rgba(60,50,120,0) 40%),
  linear-gradient(160deg,#ece9fc,#d6cff5)}
.img-launch{background:
  radial-gradient(circle at 20% 40%,rgba(60,70,160,.5),rgba(60,70,160,0) 28%),
  radial-gradient(circle at 20% 88%,rgba(240,180,40,.55),rgba(240,180,40,0) 26%),
  radial-gradient(circle at 78% 58%,rgba(70,130,220,.45),rgba(70,130,220,0) 26%),
  radial-gradient(circle at 50% 40%,rgba(245,140,130,.35),rgba(245,140,130,0) 20%),
  linear-gradient(160deg,#f2f4f9,#e3e7f2)}
.view-all{left:518px;top:2268px;width:164px;height:49px;padding-left:32px;font-size:16px}

/* contact */
.field{position:absolute;background:var(--white);box-shadow:0 1px 8px rgba(0,0,0,.09);font-size:13px;color:var(--muted);padding:15px 0 0 20px;font-weight:300}
.submit{left:109px;top:2864px;width:189px;height:57px;padding-left:27px;font-size:17px}
.contact-blob{position:absolute;left:645px;top:2453px;width:468px;height:455px;border-radius:55% 45% 50% 50%/40% 50% 50% 60%;background:linear-gradient(160deg,var(--blob-soft),var(--blob))}
.contact-screen{position:absolute;left:743px;top:2669px;width:264px;height:186px;border:8px solid #1fb6cf;border-radius:10px;
  background:
    radial-gradient(circle at 72% 58%,rgba(245,95,80,.75),rgba(245,95,80,0) 22%),
    radial-gradient(circle at 38% 58%,rgba(30,190,210,.65),rgba(30,190,210,0) 26%),
    radial-gradient(circle at 55% 35%,rgba(245,160,60,.6),rgba(245,160,60,0) 18%),
    #ffffff}
.contact-dots{position:absolute;left:915px;top:2686px;display:flex;gap:6px}
.contact-dots i{width:11px;height:11px;border-radius:50%;background:#f5a640}
.contact-dots i:first-child{background:#1fb6cf}
.contact-dots i:last-child{background:#f56a5a}

/* footer */
.site-footer{position:absolute;left:0;top:3013px;width:1200px;height:194px;background:var(--footer-bg)}
.foot-links{position:absolute;left:78px;top:56px;font-size:16px;color:var(--ink-dark)}
.foot-links span{margin:0 10px}
.mail-icon{position:absolute;left:76px;top:101px;width:40px;height:40px;border-radius:50%;background:var(--ink);display:flex;align-items:center;justify-content:center}
.mail-text{position:absolute;left:134px;top:101px;font-size:15px;line-height:19px;color:var(--ink-dark)}
.foot-mark{position:absolute;left:570px;top:36px;width:60px;height:60px;border-radius:50%;background:var(--white)}
.foot-logo{position:absolute;left:470px;top:130px;width:260px;text-align:center;font-size:26px;letter-spacing:3px;color:var(--ink)}
.newsletter-title{position:absolute;left:825px;top:56px;font-size:16px;font-weight:500;color:var(--ink-dark)}
.newsletter{position:absolute;left:822px;top:89px;width:303px;height:43px;background:var(--white);border-radius:3px}
.newsletter .ph{position:absolute;left:18px;top:14px;font-size:12px;color:var(--ink-dark)}
.newsletter .go{position:absolute;right:6px;top:5px;width:86px;height:33px;border-radius:3px;background:var(--ink);color:var(--white);font-size:13px;display:flex;align-items:center;justify-content:center}
.base-bar{position:absolute;left:0;top:3207px;width:1200px;height:49px;background:var(--bar);color:var(--white)}
.base-bar p{position:absolute;left:78px;top:17px;font-size:12px}
.social{position:absolute;top:12px;width:27px;height:27px;border-radius:50%;border:2px solid var(--white)}
</style>
</head>
<body>

<header class="site-header">
  <nav class="main-nav">
    <a class="active" style="left:674px">HOME</a>
    <a style="left:762px">ABOUT ME</a>
    <a style="left:888px">BLOG</a>
  </nav>
  <a class="btn nav-cta">CONTACT US</a>
</header>
<div class="logo-disc"></div>
<div class="logo-mark"></div>
<div class="logo-name">QUILL MOTH</div>

<section class="hero">
  <h1>BUILDING<span>BUSINESSES</span></h1>
  <p class="lede">Helping Content Creators Build Their Own Brand</p>
  <a class="btn hero-cta">CONTACT US
    <span class="arrow" style="width:40px;height:40px"><svg width="16" height="12" viewBox="0 0 16 12"><path d="M2 1l5 5-5 5M9 1l5 5-5 5" fill="none" stroke="#fff" stroke-width="2"/></svg></span>
  </a>
  <div class="hero-art"><div class="scene" role="img" aria-label="Illustration of two creators drawing on large canvases beside a potted plant"></div></div>
</section>

<section class="about">
  <div class="about-blob"></div>
  <div class="about-frame" role="img" aria-label="Illustration of two creators filming content with a camera on a tripod"></div>
  <div class="about-ground"></div>
  <h2 class="title" style="left:593px;top:891px">About Me</h2>
  <div class="rule" style="left:872px;top:923px;width:100px"></div>
  <p class="about-tag">Founded in 2024, we provide the highest level of goods and service.</p>
  <p class="about-copy">Lorem ipsum dolor sit amet, consectetur adipiscing elit. Etiam in vestibu lum urna. Quisque in lectus non sem consequat varius mattis id odio. Mauris sed libero a velit pel lentesque volutpat. Donec sed augue congue, consequat eros in, fringilla ante. Inter dum et malesuada fames ac ante ipsum primis in faucibus.</p>
  <a class="btn about-cta">READ MORE
    <span class="arrow" style="width:32px;height:32px"><svg width="14" height="10" viewBox="0 0 16 12"><path d="M2 1l5 5-5 5M9 1l5 5-5 5" fill="none" stroke="#fff" stroke-width="2"/></svg></span>
  </a>
</section>

<section class="blog">
  <div class="rule rev" style="left:365px;top:1434px;width:103px"></div>
  <h2 class="title" style="left:0;width:1200px;text-align:center;top:1404px">Our Blog</h2>
  <div class="rule" style="left:733px;top:1434px;width:103px"></div>
  <p class="blog-intro">Lorem ipsum dolor sit amet, consectetur adipiscing elit. Etiam in vestibu lum urna. Quisque in lectus non sem conse quat varius mattis id odio. Mauris sed libero a velit pel lentesque volutpat.</p>

  <article class="post-card" style="left:101px">
    <div class="post-body" style="top:36px">
      <p class="post-date"><svg width="12" height="12" viewBox="0 0 12 12"><rect x="1" y="2" width="10" height="9" fill="none" stroke="#2f5460" stroke-width="1.4"/><path d="M1 5h10M4 0v3M8 0v3" stroke="#2f5460" stroke-width="1.4"/></svg>Apr 25, 2022</p>
      <h3 class="post-title">Lorem ipsum dolor sit elit, slit tetur elit dol dolor</h3>
      <p class="post-excerpt">Lorem ipsum dolor sit amet, consec tetur adipiscing elit, sed do eiusmod tempor incididunt ut labore et dolore</p>
      <a class="btn post-btn">READ MORE<span class="arrow" style="width:23px;height:23px"><svg width="10" height="8" viewBox="0 0 16 12"><path d="M2 1l5 5-5 5M9 1l5 5-5 5" fill="none" stroke="#fff" stroke-width="2"/></svg></span></a>
    </div>
    <div class="post-img img-search" style="top:300px" role="img" aria-label="Illustration of two people searching a website on a large monitor"></div>
  </article>

  <article class="post-card" style="left:443px">
    <div class="post-img img-brand" style="top:4px" role="img" aria-label="Illustration of designers building a brand mark on a screen"></div>
    <div class="post-body" style="top:333px">
      <p class="post-date"><svg width="12" height="12" viewBox="0 0 12 12"><rect x="1" y="2" width="10" height="9" fill="none" stroke="#2f5460" stroke-width="1.4"/><path d="M1 5h10M4 0v3M8 0v3" stroke="#2f5460" stroke-width="1.4"/></svg>Apr 25, 2022</p>
      <h3 class="post-title">Lorem ipsum dolor sit elit, slit tetur elit dol dolor</h3>
      <p class="post-excerpt">Lorem ipsum dolor sit amet, consec tetur adipiscing elit, sed do eiusmod tempor incididunt ut labore et dolore</p>
      <a class="btn post-btn">READ MORE<span class="arrow" style="width:23px;height:23px"><svg width="10" height="8" viewBox="0 0 16 12"><path d="M2 1l5 5-5 5M9 1l5 5-5 5" fill="none" stroke="#fff" stroke-width="2"/></svg></span></a>
    </div>
  </article>

  <article class="post-card" style="left:785px">
    <div class="post-body" style="top:36px">
      <p class="post-date"><svg width="12" height="12" viewBox="0 0 12 12"><rect x="1" y="2" width="10" height="9" fill="none" stroke="#2f5460" stroke-width="1.4"/><path d="M1 5h10M4 0v3M8 0v3" stroke="#2f5460" stroke-width="1.4"/></svg>Apr 25, 2022</p>
      <h3 class="post-title">Lorem ipsum dolor sit elit, slit tetur elit dol dolor</h3>
      <p class="post-excerpt">Lorem ipsum dolor sit amet, consec tetur adipiscing elit, sed do eiusmod tempor incididunt ut labore et dolore</p>
      <a class="btn post-btn">READ MORE<span class="arrow" style="width:23px;height:23px"><svg width="10" height="8" viewBox="0 0 16 12"><path d="M2 1l5 5-5 5M9 1l5 5-5 5" fill="none" stroke="#fff" stroke-width="2"/></svg></span></a>
    </div>
    <div class="post-img img-launch" style="top:300px" role="img" aria-label="Illustration of a rocket launch beside creators working on laptops"></div>
  </article>

  <a class="btn view-all">VIEW ALL
    <span class="arrow" style="width:32px;height:32px"><svg width="14" height="10" viewBox="0 0 16 12"><path d="M2 1l5 5-5 5M9 1l5 5-5 5" fill="none" stroke="#fff" stroke-width="2"/></svg></span>
  </a>
</section>

<section class="contact">
  <h2 class="title" style="left:106px;top:2444px">Contact Us</h2>
  <div class="rule" style="left:421px;top:2474px;width:103px"></div>
  <div class="field" style="left:110px;top:2552px;width:223px;height:46px">First Name:</div>
  <div class="field" style="left:353px;top:2552px;width:222px;height:46px">Last Name:</div>
  <div class="field" style="left:110px;top:2618px;width:223px;height:46px">Phone:</div>
  <div class="field" style="left:353px;top:2618px;width:222px;height:46px">Email:</div>
  <div class="field" style="left:110px;top:2685px;width:465px;height:141px;padding-top:24px">Mesage:</div>
  <a class="btn submit">SUBMIT NOW
    <span class="arrow" style="width:40px;height:40px"><svg width="16" height="12" viewBox="0 0 16 12"><path d="M2 1l5 5-5 5M9 1l5 5-5 5" fill="none" stroke="#fff" stroke-width="2"/></svg></span>
  </a>
  <div class="contact-blob"></div>
  <div class="contact-screen" role="img" aria-label="Illustration of two designers arranging shapes on a large screen"></div>
  <div class="contact-dots"><i></i><i></i><i></i></div>
</section>

<footer class="site-footer">
  <p class="foot-links">Home<span>|</span>About Me<span>|</span>Blog<span>|</span>Contact Us</p>
  <div class="mail-icon"><svg width="16" height="12" viewBox="0 0 16 12"><rect x="0.5" y="0.5" width="15" height="11" fill="#fff"/><path d="M1 1l7 6 7-6" fill="none" stroke="#2f5460" stroke-width="1.4"/></svg></div>
  <p class="mail-text">EMAIL US<br>hello@quillmoth.io</p>
  <div class="foot-mark"></div>
  <div class="foot-logo">QUILL MOTH</div>
  <p class="newsletter-title">Join Our Newsletter</p>
  <div class="newsletter"><span class="ph">Enter Your Email Address</span><span class="go">Sign Up</span></div>
</footer>
<div class="base-bar">
  <p>© 2024. All Rights Reserved.</p>
  <span class="social" style="left:1057px" aria-label="Social profile"></span>
  <span class="social" style="left:1096px" aria-label="Social profile"></span>
</div>

</body>
</html>
```